business card design - photography

I am a fine art photographer. I would like to approach galleries to exhibit my work and need a business card.

The card should convey creativity and simplicity.
I would like a double sided card.

Some options:
1. An all white card with raised or embossed text or design to create a tactile finish.
2. a white and dark grey design would also work well.
3. Would be great to use my name as part of the design but not essential.
4. My name and title on the front, other details on the back of card.

The final design should be simple, minimal, elegant and innovative.
Being minimal, it will be more about texture, text size and placement.

examples of designs I would prefer provided here:
http://plimvarka.com/ideas/40-quiet-and-refined-card-layouts

I'm also open to other designs that may be unusual and unique.

Love this:
http://www.snapvelo.com/pics/morningverselog/583014927
Updates

I have uploaded a psd file after playing around in photoshop with various fonts.  I like the font (which I downloaded from glyphmorra.com called Arual) but the design probably needs some refining.  I hope this helps.  If you'd like me to change the format of the file, please let me know.

Ilvane

Target Market(s)

Art Gallery owners/administrators and customers.

Industry/Entity Type

Business

Requirements
Must have
• A unique look.

Matte, silky finish or heavy textured stock. Double-sided card.

Front:
my name
photography by

Back:
phone no
email
web address
Nice to have
• Letterpress
embrossed
Clean fonts
Should not have
• Do not use illustrations of cameras or lenses.
No frames around the card edge.

```html
<!DOCTYPE html>
<html lang="en">
<head>
<meta charset="utf-8">
<title>Ilvane Marwick – Business Card</title>
<link href="https://fonts.googleapis.com/css2?family=Quicksand:wght@300&display=swap" rel="stylesheet">
<style>
  :root {
    --backdrop: #9e9697;
    --card: #ffffff;
    --emboss-line: #d9d9d9;
    --emboss-shadow: rgba(0,0,0,0.10);
    --frame-line: #efe6bf;
    --ink-dark: #5a5a5a;
    --ink-mid: #8c8c8c;
    --ink-light: #bdbdbd;
  }
  * { margin: 0; padding: 0; box-sizing: border-box; }
  html, body { width: 1200px; height: 831px; overflow: hidden; }
  body {
    position: relative;
    background: var(--backdrop);
    font-family: "Quicksand", "Century Gothic", sans-serif;
    font-weight: 300;
  }
  .card {
    position: absolute;
    background: var(--card);
  }
  .card--back  { left: 194px; top: 18px;  width: 873px; height: 392px; }
  .card--front { left: 185px; top: 428px; width: 880px; height: 392px; }
  .emboss, .frame {
    position: absolute; left: 0; top: 0; width: 100%; height: 100%;
  }
  .contact {
    position: absolute;
    right: 260px;
    top: 158px;
    text-align: right;
    font-size: 22px;
    line-height: 28px;
    letter-spacing: 0.5px;
    white-space: nowrap;
  }
  .contact__phone { color: var(--ink-light); letter-spacing: 2px; }
  .contact__email { color: var(--ink-dark); }
  .contact__web { color: var(--ink-light); }
  .identity {
    position: absolute;
    left: 0;
    top: 166px;
    width: 100%;
    text-align: center;
  }
  .identity__name {
    font-weight: 300;
    font-size: 60px;
    line-height: 72px;
    color: var(--ink-dark);
    letter-spacing: 5px;
    white-space: nowrap;
  }
  .identity__title {
    font-size: 22px;
    line-height: 28px;
    color: var(--ink-light);
    letter-spacing: 3px;
    margin-top: 2px;
  }
</style>
</head>
<body>
  <section class="card card--back" aria-label="Card back with contact details">
    <svg class="emboss" viewBox="0 0 873 392" aria-hidden="true">
      <defs>
        <filter id="soft-back" x="-5%" y="-5%" width="110%" height="110%">
          <feGaussianBlur stdDeviation="2.5"/>
        </filter>
      </defs>
      <rect x="26" y="26" width="826" height="348" rx="78" fill="none" stroke="var(--emboss-shadow)" stroke-width="6" filter="url(#soft-back)"/>
      <rect x="24" y="23" width="826" height="348" rx="78" fill="none" stroke="var(--emboss-line)" stroke-width="2"/>
    </svg>
    <svg class="frame" viewBox="0 0 873 392" aria-hidden="true">
      <polyline points="286,148 227,148 227,259" fill="none" stroke="var(--frame-line)" stroke-width="2"/>
      <polyline points="631,167 631,274 517,274" fill="none" stroke="var(--frame-line)" stroke-width="2"/>
    </svg>
    <div class="contact">
      <p class="contact__phone">0491 572 308</p>
      <p class="contact__email">imarwick@mailora.com</p>
      <p class="contact__web">www.ilvanemarwick.com</p>
    </div>
  </section>

  <section class="card card--front" aria-label="Card front with name">
    <svg class="emboss" viewBox="0 0 880 392" aria-hidden="true">
      <defs>
        <filter id="soft-front" x="-5%" y="-5%" width="110%" height="110%">
          <feGaussianBlur stdDeviation="2.5"/>
        </filter>
      </defs>
      <rect x="26" y="27" width="834" height="342" rx="78" fill="none" stroke="var(--emboss-shadow)" stroke-width="6" filter="url(#soft-front)"/>
      <rect x="24" y="24" width="834" height="342" rx="78" fill="none" stroke="var(--emboss-line)" stroke-width="2"/>
    </svg>
    <div class="identity">
      <h1 class="identity__name">Ilvane Marwick</h1>
      <p class="identity__title">Photography by</p>
    </div>
  </section>
</body>
</html>
```